Business Card Design

We need a business card for a new business based in Sydney, Australia. It is a home based baking business, the key products are cookies and muffins and slices including gluten free baked goods. With the emphasis on home made baking. The target market is cafes, coffee shops and vans, restaurants. Products may be provided in display jars or individually wrapped. The final design should be in the colours pink, purple.

Business

Tindle's Bakery Pty Ltd, Marisa Pellow, marisa@tindlesbakery.com.au
0451 276 308, www.tindlesbakery.com.au, ACN 512 648 397,

```html
<!DOCTYPE html>
<html lang="en">
<head>
<meta charset="utf-8">
<title>Tindle's Bakery Pty Ltd – Business Card</title>
<link rel="stylesheet" href="https://fonts.googleapis.com/css2?family=Tinos:wght@700&family=Arimo:wght@400&display=swap">
<style>
  :root {
    --stage: #3b3440;
    --card-white: #ffffff;
    --plum: #8b0c97;
    --plum-text: #7a1486;
    --pink: #f466bb;
    --pink-light: #fa8fd0;
    --ink-contact: #6d1a7c;
  }
  * { margin: 0; padding: 0; box-sizing: border-box; }
  html, body {
    width: 1200px; height: 800px; overflow: hidden;
    background: var(--stage);
  }
  .stage {
    position: relative; width: 1200px; height: 800px;
  }
  .card {
    position: absolute; top: 257px;
    width: 500px; height: 286px;
    background: var(--card-white);
    overflow: hidden;
    box-shadow: 0 10px 30px rgba(0,0,0,0.35);
  }
  .card--front { left: 70px; }
  .card--back { left: 630px; }
  .card__art { position: absolute; inset: 0; width: 100%; height: 100%; }

  .brand {
    position: absolute; left: 0; right: 0;
    display: flex; align-items: center; justify-content: center; gap: 8px;
    font-family: "Tinos", "Times New Roman", serif;
    font-weight: 700; color: var(--plum-text);
    white-space: nowrap;
  }
  .brand__dot {
    border-radius: 50%; background: var(--plum);
    flex: none;
  }
  .card--front .brand { top: 96px; font-size: 26px; }
  .card--front .brand__dot { width: 16px; height: 16px; }
  .card--back .brand { top: 30px; font-size: 15px; }
  .card--back .brand__dot { width: 10px; height: 10px; }

  .person {
    position: absolute; top: 66px; left: 0; right: 0;
    text-align: center;
    font-family: "Tinos", "Times New Roman", serif;
    font-weight: 700; font-size: 24px;
    color: var(--plum-text);
  }
  .contacts {
    position: absolute; top: 112px; left: 118px;
    list-style: none;
    font-family: "Arimo", Arial, sans-serif;
    font-size: 15px; line-height: 21px;
    color: var(--ink-contact);
  }
  .contacts li { display: flex; align-items: center; gap: 6px; }
  .contacts svg { width: 11px; height: 11px; flex: none; }
</style>
</head>
<body>
<main class="stage">

  <section class="card card--front" aria-label="Card front">
    <svg class="card__art" viewBox="0 0 500 286" aria-hidden="true" preserveAspectRatio="none">
      <path d="M0 118 C110 128 200 200 330 228 C400 242 450 244 500 244 L500 286 L0 286 Z" fill="var(--pink)"/>
      <path d="M0 134 C110 146 200 214 330 240 C400 254 450 256 500 256 L500 286 L0 286 Z" fill="var(--plum)"/>
    </svg>
    <div class="brand">
      <span class="brand__dot"></span>
      <span class="brand__name">Tindle's Bakery Pty Ltd</span>
    </div>
  </section>

  <section class="card card--back" aria-label="Card back">
    <svg class="card__art" viewBox="0 0 500 286" aria-hidden="true" preserveAspectRatio="none">
      <path d="M0 70 C60 92 150 96 500 100 L500 200 C420 216 330 250 260 286 L0 286 Z" fill="var(--pink)"/>
      <path d="M0 70 C60 92 150 96 500 100 L500 106 C150 102 60 98 0 80 Z" fill="var(--pink-light)"/>
    </svg>
    <div class="brand">
      <span class="brand__dot"></span>
      <span class="brand__name">Tindle's Bakery Pty Ltd</span>
    </div>
    <h1 class="person">Marisa Pellow</h1>
    <ul class="contacts">
      <li>
        <svg viewBox="0 0 12 12" aria-hidden="true"><rect x="1" y="2.5" width="10" height="7" fill="#fff"/><path d="M1 2.5 L6 7 L11 2.5" fill="none" stroke="var(--pink)" stroke-width="1"/></svg>
        marisa@tindlesbakery.com.au
      </li>
      <li>
        <svg viewBox="0 0 12 12" aria-hidden="true"><path d="M3 1 L5 3.5 L4 5 C5 7 6 8 7.5 8.5 L9 7.5 L11 9.5 L9.5 11 C5 10.5 1.5 7 1 2.5 Z" fill="#fff"/></svg>
        0451 276 308
      </li>
      <li>
        <svg viewBox="0 0 12 12" aria-hidden="true"><circle cx="6" cy="6" r="4.5" fill="none" stroke="#fff" stroke-width="1.2"/><path d="M1.5 6 H10.5 M6 1.5 C3.5 4 3.5 8 6 10.5 M6 1.5 C8.5 4 8.5 8 6 10.5" fill="none" stroke="#fff" stroke-width="0.8"/></svg>
        www.tindlesbakery.com.au
      </li>
      <li>
        <svg viewBox="0 0 12 12" aria-hidden="true"><path d="M6 11 C3 7.5 2 6 2 4.5 A4 4 0 0 1 10 4.5 C10 6 9 7.5 6 11 Z" fill="#fff"/><circle cx="6" cy="4.5" r="1.4" fill="var(--pink)"/></svg>
        ACN 512 648 397
      </li>
    </ul>
  </section>

</main>
</body>
</html>
```